Lead Generation Postcard for Psychotherapists

I am a marketing coach for therapists in private practice. I am creating a lead generation postcard to send to psychotherapists that are not currently familiar with my services.

I'm offering them a free cheat sheet called, "7 Keys to a Patient-Winning Homepage for Psychotherapists". The goal of the postcard is to get clicks to the URL and get the cheat sheet.The URL is www.MeadowlarkCounselHub.com/Insights (not live yet)

Target Market(s)

Psychotherapists in private practice

Industry/Entity Type

Marketing

Requirements
Must have
• Postcard size is 8.52" x 5.47"
• Here are the dimensions: Full Bleed Size
• 8.64" x 5.59"
• 219 x 142 mm
• 2592 x 1677 pixels
• Document Trim Size
• 8.52" x 5.47"
• 216 x 139 mm
• 2556 x 1642 pixels
• This link provides more information about the requirements: http://www.quillpressa.com/vp/ns/propath/UploadResources.aspx?pfid=126
• The BACK of the postcard must adhere to this template: http://www.quillpressa.com/vp/images/template_files/Quillpressa_MailingServices.pdf (Use the bottom template, for the larger postcard.)
Nice to have
• I'd like to have my photo on the back of the postcard, I've included several for you to choose from.
Should not have
• Nothing too "corporate" or "techie" looking

```html
<!DOCTYPE html>
<html lang="en">
<head>
<meta charset="utf-8">
<title>Patient-Winning Homepage Postcard</title>
<link href="https://fonts.googleapis.com/css2?family=Open+Sans:ital,wght@0,400;0,600;0,700;0,800;1,400&family=Oswald:wght@500;700&display=swap" rel="stylesheet">
<style>
:root{
  --navy:#0f2f6b;
  --blue:#1a4f9c;
  --sky:#2f74c8;
  --red:#d3262b;
  --gold:#f6c51d;
  --grey:#e4e6ea;
  --ink:#2b2b2b;
  --page:#eef0f2;
  --white:#ffffff;
}
*{box-sizing:border-box;margin:0;padding:0}
html,body{width:857px;height:1200px;overflow:hidden;background:var(--page);font-family:"Open Sans",Arial,sans-serif;color:var(--ink)}
.card{position:absolute;left:63px;width:732px;height:498px;background:var(--white);box-shadow:0 6px 14px rgba(0,0,0,.25);overflow:hidden}
.card--front{top:51px}
.card--back{top:660px}

.brand{position:absolute;display:flex;align-items:center;gap:8px;font-weight:800;color:var(--navy);font-size:15px;line-height:1.05;text-transform:uppercase;letter-spacing:.5px}
.brand__dot{width:22px;height:22px;border-radius:50%;background:var(--gold);flex:none}

/* front */
.card--front .brand{left:30px;top:30px}
.offer{position:absolute;left:28px;top:120px;width:260px;font-family:"Oswald",Impact,sans-serif;font-weight:700;color:var(--sky);line-height:.95}
.offer__free{font-size:92px;display:block}
.offer__sheet{font-size:58px;display:block;color:var(--navy)}
.exclusive{position:absolute;left:20px;top:340px;width:270px;background:var(--red);color:var(--white);font-weight:800;font-size:26px;line-height:1.1;padding:10px 16px;transform:rotate(-2deg)}
.binding{position:absolute;left:300px;top:0;width:20px;height:498px;background:linear-gradient(90deg,#c9ccd2,#f3f4f6)}
.panel{position:absolute;left:320px;top:0;width:412px;height:498px;background:linear-gradient(180deg,var(--blue),var(--navy))}
.panel__title{padding:18px 22px 10px;color:var(--white);font-family:"Oswald",Impact,sans-serif;font-weight:500;font-size:30px;line-height:1.05}
.panel__title em{font-style:normal;color:var(--gold);font-size:40px;display:block}
.audience{background:var(--grey);color:var(--navy);font-weight:700;font-size:14px;padding:7px 22px;word-spacing:4px}
.panel__ask{color:var(--white);font-weight:800;font-size:21px;padding:12px 22px 8px}
.pains{list-style:none;padding:0 22px}
.pains li{display:flex;gap:8px;color:var(--white);font-size:11.5px;line-height:1.35;margin-bottom:8px}
.pains svg{flex:none;margin-top:1px}
.panel__copy{color:var(--white);font-size:11.5px;line-height:1.4;padding:6px 22px 0}
.panel__cta{color:var(--gold);font-weight:700;font-size:13px;line-height:1.35;padding:14px 22px 0}

/* back */
.card--back .brand{left:30px;top:30px}
.portrait{position:absolute;left:330px;top:40px;width:104px;height:104px;border-radius:50%;background:radial-gradient(circle at 50% 40%,#d8b79c,#7a5a45)}
.bio{position:absolute;left:450px;top:44px;width:260px;font-size:11.5px;line-height:1.4}
.bio strong{color:var(--red)}
.back-body{position:absolute;left:30px;top:196px;width:560px;display:flex;flex-direction:column;gap:10px}
.hook{font-weight:800;font-size:24px;line-height:1.15;color:var(--sky)}
.hook b{color:var(--red)}
.story{font-size:9.5px;line-height:1.4}
.story p{margin-bottom:6px}
.story p:last-child{margin-bottom:0}
.story__cta{font-weight:700;font-size:12px;line-height:1.35;color:var(--sky)}
</style>
</head>
<body>

<section class="card card--front">
  <div class="brand"><span class="brand__dot"></span><span>Meadowlark<br>Counsel Hub</span></div>
  <h2 class="offer"><span class="offer__free">FREE</span><span class="offer__sheet">CHEAT SHEET</span></h2>
  <div class="exclusive">Exclusively for Psychotherapists</div>
  <div class="binding" role="img" aria-label="Notebook spiral binding"></div>
  <div class="panel">
    <h1 class="panel__title"><em>7 Keys to</em>A Patient-Winning Homepage</h1>
    <div class="audience">Psychotherapists | Psychologists | Counselors</div>
    <p class="panel__ask">Does this sound familiar?</p>
    <ul class="pains">
      <li><svg width="13" height="13" viewBox="0 0 13 13"><rect x=".5" y=".5" width="12" height="12" fill="none" stroke="#fff"/><path d="M3 6.5l2.5 2.5L10 3.5" stroke="#f6c51d" stroke-width="2" fill="none"/></svg>You spent thousands to build a website but the phone still isn't ringing</li>
      <li><svg width="13" height="13" viewBox="0 0 13 13"><rect x=".5" y=".5" width="12" height="12" fill="none" stroke="#fff"/><path d="M3 6.5l2.5 2.5L10 3.5" stroke="#f6c51d" stroke-width="2" fill="none"/></svg>Potential clients that find you online are all "price shoppers", not ideal clients serious about working with you</li>
      <li><svg width="13" height="13" viewBox="0 0 13 13"><rect x=".5" y=".5" width="12" height="12" fill="none" stroke="#fff"/><path d="M3 6.5l2.5 2.5L10 3.5" stroke="#f6c51d" stroke-width="2" fill="none"/></svg>You know your website needs a serious facelift, but have no idea what to do or where to start the process</li>
    </ul>
    <p class="panel__copy">If you can relate to any of these, then you're going to LOVE the "7 Keys to a Patient-Winning Homepage" Cheat Sheet. In this easy to follow guide, you'll discover what's working <strong>RIGHT NOW</strong> to attract more ideal clients online.</p>
    <p class="panel__cta">Visit www.MeadowlarkCounselHub.com/Insights<br>before October 25th to get your copy.</p>
  </div>
</section>

<section class="card card--back">
  <div class="brand"><span class="brand__dot"></span><span>Meadowlark<br>Counsel Hub</span></div>
  <div class="portrait" role="img" aria-label="Portrait photo of the practice-building coach"></div>
  <p class="bio"><strong>Dana Whitcombe</strong>, LMFT, is a best-selling author and practice-building strategist serving thousands of therapists worldwide. She specializes in helping therapists build 6-figure practices doing the work they love.</p>
  <div class="back-body">
    <h2 class="hook">Is your website <b>COSTING</b> you<br>clients instead of attracting them?</h2>
    <div class="story">
      <p>Most therapists don't have any idea what it takes to build a client-attracting website, so they either hand the whole thing off to a "professional" designer, or they attempt to do it themselves. The problem with both of these solutions is that you're hoping for the best, rather than strategically creating an online marketing process. Just like most of you don't know how to build a website, most web designers don't know what it takes to attract psychotherapy clients.</p>
      <p>Rather than continuing to be disappointed in the results of your online marketing, why not learn EXACTLY what it takes to effectively market your private practice online?</p>
      <p>The FREE Cheat Sheet "7 Keys to a Patient-Winning Homepage" does just that. If you're ready to start seeing REAL RESULTS from your online marketing, grab your copy today.</p>
    </div>
    <p class="story__cta">Visit www.MeadowlarkCounselHub.com/Insights<br>before October 25th to get your copy.</p>
  </div>
</section>

</body>
</html>
```